Maple Hollow Pet Services ABN 71 493 260 518 needs a Postcard Design

Genuine pet lover offering a professional and highly personalised pet service. I will visit your home daily to care for your pet in their own environment. THE OTHER OPTION FOR WHEN YOU GO ON HOLIDAYS. Dog Holiday Service (includes but not limited to) Feed, Water, Walk, Love & Play. Clean Litter Trays, Hutches & Cages. Administer Medication as Directed. Water Pot Plants & Collec Mail. Individual Dog Walking (Permanent or Casual). REASONABLE RATES. Police Check & References available upon request. Contact HARRIET 0412 684 219

```html
<!DOCTYPE html>
<html lang="en">
<head>
<meta charset="utf-8">
<title>Maple Hollow Pet Services Postcard</title>
<link href="https://fonts.googleapis.com/css2?family=Oswald:wght@300;400&family=Lato:wght@300;400;700&display=swap" rel="stylesheet">
<style>
  :root {
    --backdrop: #a7a7a7;
    --card: #ffffff;
    --orange: #e67e22;
    --brand-red: #b3171c;
    --ink: #1e1e1e;
    --muted: #8f8f8f;
    --rule: #9a9a9a;
    --tick: #e8722a;
  }
  * { margin: 0; padding: 0; box-sizing: border-box; }
  html, body { width: 1200px; height: 1100px; overflow: hidden; }
  body { background: var(--backdrop); position: relative; font-family: "Lato", sans-serif; }

  .postcard-front { position: absolute; left: 272px; top: 28px; width: 656px; height: 508px; background: var(--card); }
  .photo { position: absolute; }
  .photo--kittens { left: 0; top: 0; width: 343px; height: 198px;
    background: linear-gradient(135deg, #8e7fb6 0%, #b3a6d3 45%, #6b6070 70%, #9a86c0 100%); }
  .photo--rabbit { left: 349px; top: 0; width: 307px; height: 198px;
    background: linear-gradient(160deg, #8a6a4e 0%, #6c4d35 40%, #b18456 65%, #d6c08a 100%); }
  .photo--dog { left: 0; top: 285px; width: 656px; height: 223px;
    background: linear-gradient(100deg, #5f6f7e 0%, #45553e 28%, #c08a4a 45%, #b67c3d 58%, #7d8a55 78%, #8b9462 100%); }

  .title-band { position: absolute; left: 0; top: 203px; width: 656px; height: 77px; background: var(--orange); }
  .title-band__headline { position: absolute; left: 0; right: 0; top: 1px; text-align: center;
    font-family: "Oswald", sans-serif; font-weight: 400; font-size: 32px; line-height: 52px; color: #fff; letter-spacing: -0.4px; }
  .title-band__tagline { position: absolute; right: 38px; top: 47px;
    font-family: "Lato", sans-serif; font-weight: 700; font-size: 18px; line-height: 22px; color: var(--brand-red); }

  .postcard-back { position: absolute; left: 273px; top: 558px; width: 655px; height: 508px; background: var(--card); }
  .intro { position: absolute; left: 18px; top: 15px; width: 298px; text-align: center;
    font-size: 15.5px; line-height: 20px; color: var(--ink); }
  .holiday-heading { position: absolute; left: 18px; top: 71px; width: 298px; text-align: center;
    font-weight: 400; font-size: 16px; line-height: 20px; color: var(--brand-red); }
  .divider { position: absolute; left: 317px; top: 64px; width: 1px; height: 350px; background: var(--rule); }

  .services { list-style: none; position: absolute; left: 20px; top: 124px; width: 290px; }
  .services li { position: relative; padding-left: 31px; font-weight: 300; font-size: 14px; line-height: 18px; color: var(--muted); }
  .services svg { position: absolute; left: 0; top: 2px; }

  .contact { position: absolute; left: 27px; top: 379px; display: flex; align-items: center; gap: 9px;
    white-space: nowrap; transform: scaleX(0.9); transform-origin: left center;
    font-family: "Oswald", sans-serif; font-weight: 300; font-size: 26px; line-height: 34px; color: var(--brand-red); letter-spacing: -0.5px; }

  .stamp-box { position: absolute; left: 499px; top: 24px; width: 134px; height: 134px; border: 1.5px solid #9c9c9c; }
  .address-line { position: absolute; left: 343px; width: 268px; height: 1px; background: var(--rule); }
</style>
</head>
<body>
  <section class="postcard-front">
    <div class="photo photo--kittens" role="img" aria-label="Photo of two sleepy tabby kittens on a lilac blanket"></div>
    <div class="photo photo--rabbit" role="img" aria-label="Photo of a brown rabbit sitting in straw inside a hutch"></div>
    <div class="title-band">
      <h1 class="title-band__headline">A Professional and Highly Personalised Pet Service</h1>
      <p class="title-band__tagline">from a genuine pet lover</p>
    </div>
    <div class="photo photo--dog" role="img" aria-label="Photo of a golden labrador lying on grass beside a wooden fence"></div>
  </section>

  <section class="postcard-back">
    <p class="intro">I will visit your home daily to care for your pet in their own environment.</p>
    <h2 class="holiday-heading">THE OTHER OPTION FOR WHEN YOU GO ON HOLIDAYS.</h2>
    <div class="divider"></div>

    <ul class="services">
      <li style="margin-bottom:9px"><svg width="20" height="17" viewBox="0 0 20 17"><rect x="1" y="3" width="13" height="13" fill="none" stroke="var(--tick)" stroke-width="2"/><path d="M4 9l4 4 10-12" fill="none" stroke="var(--tick)" stroke-width="2.5"/></svg>Dog Holiday Service (includes but not limited to) Feed, Water, Walk, Love &amp; Play.</li>
      <li style="margin-bottom:10px"><svg width="20" height="17" viewBox="0 0 20 17"><rect x="1" y="3" width="13" height="13" fill="none" stroke="var(--tick)" stroke-width="2"/><path d="M4 9l4 4 10-12" fill="none" stroke="var(--tick)" stroke-width="2.5"/></svg>Clean Litter Trays, Hutches &amp; Cages.</li>
      <li style="margin-bottom:12px"><svg width="20" height="17" viewBox="0 0 20 17"><rect x="1" y="3" width="13" height="13" fill="none" stroke="var(--tick)" stroke-width="2"/><path d="M4 9l4 4 10-12" fill="none" stroke="var(--tick)" stroke-width="2.5"/></svg>Administer Medication as Directed.</li>
      <li style="margin-bottom:10px"><svg width="20" height="17" viewBox="0 0 20 17"><rect x="1" y="3" width="13" height="13" fill="none" stroke="var(--tick)" stroke-width="2"/><path d="M4 9l4 4 10-12" fill="none" stroke="var(--tick)" stroke-width="2.5"/></svg>Water Pot Plants &amp; Collect Mail.</li>
      <li style="margin-bottom:12px"><svg width="20" height="17" viewBox="0 0 20 17"><rect x="1" y="3" width="13" height="13" fill="none" stroke="var(--tick)" stroke-width="2"/><path d="M4 9l4 4 10-12" fill="none" stroke="var(--tick)" stroke-width="2.5"/></svg>Individual Dog Walking (Permanent or Casual).</li>
      <li style="margin-bottom:12px"><svg width="20" height="17" viewBox="0 0 20 17"><rect x="1" y="3" width="13" height="13" fill="none" stroke="var(--tick)" stroke-width="2"/><path d="M4 9l4 4 10-12" fill="none" stroke="var(--tick)" stroke-width="2.5"/></svg>REASONABLE RATES.</li>
      <li><svg width="20" height="17" viewBox="0 0 20 17"><rect x="1" y="3" width="13" height="13" fill="none" stroke="var(--tick)" stroke-width="2"/><path d="M4 9l4 4 10-12" fill="none" stroke="var(--tick)" stroke-width="2.5"/></svg>Police Check &amp; References available upon request.</li>
    </ul>

    <p class="contact">
      <svg width="22" height="22" viewBox="0 0 22 22" aria-hidden="true"><circle cx="11" cy="11" r="9.5" fill="none" stroke="#8a8a8a" stroke-width="1.3"/><path d="M8 6.5c-1 .6-1.4 1.6-1 3 .7 2.4 2.6 4.6 4.8 5.6 1.3.6 2.3.3 3-.6l-1.8-1.6-1.1.7c-1-.5-2-1.6-2.5-2.7l.8-1z" fill="#8a8a8a"/></svg>
      <span class="contact__text">Contact HARRIET 0412 684 219</span>
    </p>

    <div class="stamp-box"></div>
    <div class="address-line" style="top:242px"></div>
    <div class="address-line" style="top:274px"></div>
    <div class="address-line" style="top:306px"></div>
    <div class="address-line" style="top:339px"></div>
    <div class="address-line" style="top:371px"></div>
  </section>
</body>
</html>
```